Kelvo Auto - help to get me noticed

We not long ago tasked Pixel Harbour to design a logo for my business. I'm happy with the result so would like to have a business card designed as a follow up.

It's an Automotive service and repair business that offers the following -
- Servicing
- General repairs
- Brakes
- Detailing
- Integrity

Kelvo Automotive
Dallin Mereth
0471 926 317

Target Market(s)

Everyday people with the ability to reach out to corporate customers also.

Industry/Entity Type

Automotive

Contact Information for Business Card

Black card, logo, name and phone number on front. Other details on back of card.

```html
<!DOCTYPE html>
<html lang="en">
<head>
<meta charset="utf-8">
<title>Kelvo Automotive – Business Card</title>
<link rel="stylesheet" href="https://fonts.googleapis.com/css2?family=Roboto:wght@400;500;700&display=swap">
<style>
  :root {
    --backdrop: #2b2b2d;
    --card: #08090b;
    --lime: #a6e23a;
    --lime-deep: #5fc02a;
    --white: #f2f2f2;
    --ink: #15170f;
  }
  * { margin: 0; padding: 0; box-sizing: border-box; }
  html, body {
    width: 1200px; height: 800px; overflow: hidden;
    background: var(--backdrop);
    font-family: "Roboto", Arial, sans-serif;
  }
  .stage {
    width: 1200px; height: 800px;
    display: flex; flex-direction: column; align-items: center; justify-content: center;
    gap: 40px;
  }
  .card {
    position: relative;
    width: 560px; height: 340px;
    background: var(--card);
    overflow: hidden;
    box-shadow: 0 14px 30px rgba(0,0,0,0.45);
  }
  .brand {
    position: absolute;
    color: var(--lime);
    font-weight: 700;
    text-transform: uppercase;
    line-height: 1;
    text-align: center;
  }
  .brand__name { display: block; font-size: 40px; letter-spacing: 1px; }
  .brand__line { display: block; font-size: 14px; letter-spacing: 2.5px; margin-top: 4px; }
  .card--front .brand { top: 34px; right: 60px; }
  .holder {
    position: absolute; left: 70px; bottom: 66px;
    color: var(--white);
  }
  .holder__name { font-size: 22px; font-weight: 500; letter-spacing: 0.5px; text-transform: uppercase; }
  .holder__phone { font-size: 15px; margin-top: 6px; letter-spacing: 0.8px; }

  .accent-block {
    position: absolute; left: 0; top: 176px;
    width: 30px; height: 50px;
    background: linear-gradient(to bottom, var(--lime), var(--lime-deep));
  }
  .card--back .brand { left: 82px; top: 172px; }
  .services {
    position: absolute; right: 0; top: 116px;
    width: 278px; height: 70px;
    background: linear-gradient(to bottom, var(--lime), var(--lime-deep));
    color: var(--ink);
    display: flex; flex-direction: column; justify-content: center;
    padding-left: 26px;
    font-size: 12.5px; font-weight: 500; letter-spacing: 0.5px;
    text-transform: uppercase; line-height: 1.45;
  }
</style>
</head>
<body>
<main class="stage">
  <section class="card card--front" aria-label="Card front">
    <div class="brand">
      <span class="brand__name">Kelvo</span>
      <span class="brand__line">Automotive</span>
    </div>
    <div class="holder">
      <p class="holder__name">Dallin Mereth</p>
      <p class="holder__phone">0471 926 317</p>
    </div>
  </section>

  <section class="card card--back" aria-label="Card back">
    <div class="accent-block"></div>
    <div class="brand">
      <span class="brand__name">Kelvo</span>
      <span class="brand__line">Automotive</span>
    </div>
    <div class="services">
      <p>Servicing | General Repairs</p>
      <p>Brakes | Detailing | Integrity</p>
    </div>
  </section>
</main>
</body>
</html>
```